Business Card template - vertical layout

Design a vertical business card template to my exisiting specifications with examples shown.
This is a business card template and I need to flexibility to change the company logo and details myself in future.
The main colour scheme is blue, white, grey.
Clean, professional designs would be appreciated.
Business
The format is double sided, vertical layout as shown in the example image.
The business card is going to be a template design which means I need to be able to change the company logo and details on side B myself in future.
Side A:
company logo with blue background (as shown in the example image, same blue colour)
Side B:
company logo on the top
personal name (Leo Dorsey)
job title (Chief Executive Officer)
mobile phone number (+61 455 210 739)
email: (leo.dorsey@kelvarogen.com.au)
wechat: (leodorsey8)
PO Box address (PO Box 27415 Melbourne VIC 3001)
Office address: (482 Harrow Street Melbourne VIC 3008 Australia)
office address 2: (Level 2, 9 Tamsin Street Burwood NSW 2134)

```html
<!DOCTYPE html>
<html lang="en">
<head>
<meta charset="utf-8">
<title>Kelvarogen Business Card – Vertical Template</title>
<link rel="stylesheet" href="https://fonts.googleapis.com/css2?family=Montserrat:wght@400;500;700&family=Open+Sans:wght@400&display=swap">
<style>
  :root {
    --bg: #ebebeb;
    --blue: #4d7bbb;
    --blue-deep: #3a68ab;
    --blue-light: #6fb6e0;
    --white: #ffffff;
    --green: #8cc04b;
    --ink: #3f6aa8;
    --shadow: rgba(0, 0, 0, 0.18);
  }
  html, body {
    margin: 0;
    padding: 0;
    width: 1200px;
    height: 814px;
    overflow: hidden;
    background: var(--bg);
  }
  .canvas {
    position: relative;
    width: 1200px;
    height: 814px;
  }
  .card {
    position: absolute;
    top: 137px;
    width: 330px;
    height: 540px;
    background: var(--white);
    box-shadow: 0 14px 30px var(--shadow);
    overflow: hidden;
  }
  .card--front { left: 220px; }
  .card--back  { left: 650px; }
  .card__art {
    position: absolute;
    inset: 0;
    width: 100%;
    height: 100%;
  }
  .logo-text {
    position: absolute;
    font-family: "Open Sans", sans-serif;
    font-weight: 400;
    letter-spacing: -0.5px;
    white-space: nowrap;
  }
  .card--front .logo-text {
    left: 0;
    right: 0;
    top: 232px;
    text-align: center;
    font-size: 46px;
    color: var(--white);
  }
  .card--back .logo-text {
    left: 30px;
    top: 112px;
    font-size: 48px;
    color: var(--ink);
  }
  .person {
    position: absolute;
    left: 30px;
    top: 188px;
    font-family: "Montserrat", sans-serif;
  }
  .person__name {
    margin: 0;
    font-size: 27px;
    font-weight: 700;
    color: var(--green);
    line-height: 1;
  }
  .person__title {
    margin: 5px 0 0;
    font-size: 11px;
    font-weight: 400;
    color: var(--ink);
  }
  .contacts {
    position: absolute;
    left: 30px;
    top: 256px;
    margin: 0;
    padding: 0;
    list-style: none;
    font-family: "Montserrat", sans-serif;
    font-size: 12px;
    color: var(--ink);
  }
  .contacts__item {
    display: flex;
    align-items: center;
    gap: 9px;
    height: 22px;
  }
  .contacts__icon {
    width: 13px;
    height: 13px;
    flex: none;
  }
  .contacts__address {
    margin: 0;
    padding: 0 0 0 22px;
    list-style: none;
  }
  .contacts__address li {
    line-height: 14px;
    margin-top: 7px;
  }
  .website {
    position: absolute;
    right: 22px;
    bottom: 22px;
    font-family: "Montserrat", sans-serif;
    font-size: 13px;
    font-weight: 500;
    color: var(--white);
  }
</style>
</head>
<body>
<main class="canvas">

  <!-- Side A -->
  <section class="card card--front" aria-label="Card front">
    <svg class="card__art" viewBox="0 0 330 540" preserveAspectRatio="none" aria-hidden="true">
      <defs>
        <linearGradient id="frontBlue" x1="0" y1="0" x2="1" y2="1">
          <stop offset="0" stop-color="#5c88c4"/>
          <stop offset="1" stop-color="#3f6dae"/>
        </linearGradient>
      </defs>
      <path d="M0 140 C 90 70 200 25 330 0 L330 405 C 230 470 120 515 0 540 Z" fill="url(#frontBlue)"/>
    </svg>
    <div class="logo-text">logo here</div>
  </section>

  <!-- Side B -->
  <section class="card card--back" aria-label="Card back">
    <svg class="card__art" viewBox="0 0 330 540" preserveAspectRatio="none" aria-hidden="true">
      <path class="band band--top-accent" d="M0 0 L330 0 L330 26 C 220 44 100 70 0 104 Z" fill="var(--blue-light)"/>
      <path class="band band--top" d="M0 0 L330 0 L330 20 C 220 36 100 60 0 94 Z" fill="var(--blue)"/>
      <path class="band band--bottom-accent" d="M0 540 L330 540 L330 414 C 230 450 110 495 0 514 Z" fill="var(--blue-light)"/>
      <path class="band band--bottom" d="M0 540 L330 540 L330 424 C 230 460 110 505 0 526 Z" fill="var(--blue)"/>
    </svg>

    <div class="logo-text">logo here</div>

    <div class="person">
      <p class="person__name">Leo Dorsey</p>
      <p class="person__title">Chief Executive Officer</p>
    </div>

    <ul class="contacts">
      <li class="contacts__item">
        <svg class="contacts__icon" viewBox="0 0 14 14" aria-hidden="true"><circle cx="7" cy="7" r="7" fill="var(--green)"/><path d="M4.5 3.8 L6 3.6 L6.6 5.4 L5.8 6 Q6.4 7.6 8 8.2 L8.6 7.4 L10.4 8 L10.2 9.5 Q6 10 4.5 3.8 Z" fill="#fff"/></svg>
        <span>+61 455 210 739</span>
      </li>
      <li class="contacts__item">
        <svg class="contacts__icon" viewBox="0 0 14 14" aria-hidden="true"><rect x="1" y="3" width="12" height="8" fill="var(--green)"/><path d="M1 3 L7 8 L13 3" fill="none" stroke="#fff" stroke-width="1.2"/></svg>
        <span>leo.dorsey@kelvarogen.com.au</span>
      </li>
      <li class="contacts__item">
        <svg class="contacts__icon" viewBox="0 0 14 14" aria-hidden="true"><circle cx="7" cy="7" r="7" fill="var(--green)"/><ellipse cx="7" cy="6.8" rx="3.8" ry="2.9" fill="#fff"/></svg>
        <span>leodorsey8</span>
      </li>
      <li class="contacts__item">
        <svg class="contacts__icon" viewBox="0 0 14 14" aria-hidden="true"><path d="M1 7 L7 1.5 L13 7 L11.5 7 L11.5 13 L8.3 13 L8.3 9 L5.7 9 L5.7 13 L2.5 13 L2.5 7 Z" fill="var(--green)"/></svg>
        <span>PO Box 27415 Melbourne VIC 3001</span>
      </li>
      <li>
        <ul class="contacts__address">
          <li>482 Harrow Street Melbourne<br>VIC 3008 Australia</li>
          <li>Level 2, 9 Tamsin Street Burwood<br>NSW 2134</li>
        </ul>
      </li>
    </ul>

    <div class="website">www.kelvarogen.com</div>
  </section>

</main>
</body>
</html>
```